Business Card Design

we are a wellness center offering therapeutic massage modalities and yoga and meditation classes. I would like to see designs that incorporate the colors of my current logo (image uploaded) BUT I would like to change my logo slightly so that the three words wrapping around my image are: massage yoga wellness (in other words, take out skin).

Industry/Entity Type

Massage

Contact Information for Business Card

Lena R. Vasquez, BS, CMT, E-RYT, Owner
427 E. Dalton Ave., Suite 3C
Hampton, VA 23681
757-302-5947 (office)
757-541-2086 (cell)
calmharborstudio.net
calmharborstudio@mailbox-example.net

Requirements
Nice to have
• I'd like to have my logo as a watermark on the back side, but if that's not doable, no big deal. Thanks.

```html
<!DOCTYPE html>
<html lang="en">
<head>
<meta charset="utf-8">
<title>Calm Harbor Studio — Business Card</title>
<link rel="stylesheet" href="https://fonts.googleapis.com/css2?family=Arimo:wght@400;700&display=swap">
<style>
  :root {
    --backdrop: #7e8a89;
    --card: #141618;
    --accent-orange: #f2a31b;
    --text-white: #ffffff;
    --text-soft: #e4e4e4;
    --wave-red: #d00000;
    --wave-purple: #4c06a8;
  }
  html, body {
    margin: 0;
    padding: 0;
    width: 1200px;
    height: 702px;
    overflow: hidden;
    background: var(--backdrop);
    font-family: "Arimo", Arial, sans-serif;
  }
  .business-card {
    position: absolute;
    left: 61px;
    top: 55px;
    width: 1084px;
    height: 589px;
    background: var(--card);
    overflow: hidden;
    box-shadow: 2px 3px 6px rgba(0,0,0,0.35);
  }
  .wave {
    position: absolute;
    left: 0;
    top: 0;
    width: 1084px;
    height: 589px;
  }
  .wave .band-red { fill: var(--wave-red); }
  .wave .band-purple { fill: var(--wave-purple); }
  .text-line {
    position: absolute;
    margin: 0;
    white-space: nowrap;
    line-height: 1;
  }
  .holder-name {
    left: 72px;
    top: 46px;
    font-size: 62px;
    font-weight: 400;
    color: var(--text-white);
  }
  .holder-name .given {
    color: var(--accent-orange);
    font-weight: 700;
  }
  .holder-role {
    left: 206px;
    top: 138px;
    font-size: 40px;
    font-weight: 700;
    color: var(--text-soft);
  }
  .divider {
    position: absolute;
    left: 699px;
    top: 56px;
    width: 3px;
    height: 180px;
    background: var(--text-white);
  }
  .credentials {
    position: absolute;
    left: 724px;
    top: 50px;
    margin: 0;
    padding: 0;
    list-style: none;
    color: var(--text-white);
    font-size: 30px;
    line-height: 36px;
  }
  .phones {
    position: absolute;
    left: 724px;
    top: 172px;
    margin: 0;
    color: var(--text-white);
    font-weight: 700;
    line-height: 37px;
  }
  .phones .label { font-size: 28px; }
  .phones .value { font-size: 22px; }
  .address {
    position: absolute;
    left: 63px;
    top: 340px;
    margin: 0;
    font-style: normal;
    font-weight: 700;
    font-size: 28px;
    line-height: 37px;
    color: var(--text-white);
  }
  .web-contact {
    position: absolute;
    left: 492px;
    top: 504px;
    margin: 0;
    color: var(--text-white);
    font-weight: 700;
    line-height: 36px;
  }
  .web-contact .label { font-size: 27px; }
  .web-contact .value { font-size: 21px; }
</style>
</head>
<body>
  <main class="business-card">
    <svg class="wave" viewBox="0 0 1084 589" aria-hidden="true">
      <path class="band-red" d="M0,514 C380,484 540,450 650,395 C790,332 940,323 1084,323 L1084,589 L0,589 Z"/>
      <path class="band-purple" d="M0,553 C390,532 560,486 680,424 C820,358 950,341 1084,341 L1084,589 L0,589 Z"/>
    </svg>

    <h1 class="text-line holder-name"><span class="given">Lena R.</span> Vasquez</h1>
    <p class="text-line holder-role">owner</p>

    <div class="divider"></div>
    <ul class="credentials">
      <li>BS</li>
      <li>CMT</li>
      <li>E-RYT</li>
    </ul>
    <p class="phones">
      <span class="label">Office:</span> <span class="value">757-302-5947</span><br>
      <span class="label">Cell:</span> <span class="value">757-541-2086</span>
    </p>

    <address class="address">
      427 E. Dalton Ave.,<br>
      Suite 3C Hampton,<br>
      VA 23681.
    </address>

    <p class="web-contact">
      <span class="label">URL:</span> <span class="value">calmharborstudio.net</span><br>
      <span class="label">E-Mail:</span> <span class="value">calmharborstudio@mailbox-example.net</span>
    </p>
  </main>
</body>
</html>
```